Business Card Design

Bramwell Pantry is the name of my health coaching business. My tag line is "Where good health meets real life." I will be working with clients one-on-one and in groups. My target clients are women "of a certain age" who want to be more comfortable in their own skin. We will work together in a 6-month program. The coaching sessions will take place in my kitchen. I will also be conducting monthly cooking classes and field trips - to farmer's markets, speciality markets etc.. for my clients.
Updates

the business name is Bramwell Pantry - I'm not sure how the p got in there at the end of the name

Thank you

Please include the website - www.bramwellpantry-example.com and the tag line:

Where good health meets real life on the business card.

Thank you

Please add the phone number to the business card - sorry, I forgot to state that in the original brief

(555) 218-4476

Target Market(s)

Women "of a certain age" who want to be more comfortable in their own skin

Industry/Entity Type

Cooking

Contact Information for Business Card

Bramwell Pantry
Where good health meets real life

Harriet Dunmore
Health Coach
(555) 218-4476

Font styles to use
Serif
Sans Serif

Requirements
Must have
• front & back design
I typical like soft colors - and have tended toward greens over time - I'm open although I would not like bright reds, yellows etc..

```html
<!DOCTYPE html>
<html lang="en">
<head>
<meta charset="utf-8">
<title>Bramwell Pantry – Business Card</title>
<link rel="stylesheet" href="https://fonts.googleapis.com/css2?family=Open+Sans:wght@400;600&display=swap">
<style>
  :root {
    --bg: #1b1b1b;
    --green: #2f9e35;
    --green-light: #48bf45;
    --green-dark: #23832a;
    --ink: #1a1a1a;
    --paper: #ffffff;
    --rule: #9a9a9a;
  }
  * { margin: 0; padding: 0; box-sizing: border-box; }
  html, body { width: 1200px; height: 900px; overflow: hidden; }
  body {
    background: var(--bg);
    font-family: "Open Sans", Arial, sans-serif;
    position: relative;
  }
  .card {
    position: absolute;
    left: 337px;
    width: 525px;
    height: 300px;
    border-radius: 18px;
    overflow: hidden;
  }
  /* Front */
  .card-front {
    top: 105px;
    background: linear-gradient(150deg, var(--green-light) 0%, var(--green) 55%, var(--green-dark) 100%);
    color: var(--paper);
  }
  .front-brand {
    position: absolute;
    left: 0; right: 0; top: 108px;
    text-align: center;
    font-size: 40px;
    font-weight: 400;
    letter-spacing: 0.5px;
  }
  .front-tagline {
    position: absolute;
    left: 0; right: 0; top: 172px;
    text-align: center;
    font-size: 14px;
    letter-spacing: 0.3px;
  }
  /* Back */
  .card-back {
    top: 495px;
    background: var(--paper);
    color: var(--ink);
  }
  .back-wave { position: absolute; left: 0; top: 0; width: 525px; height: 300px; }
  .person { position: absolute; left: 30px; top: 70px; }
  .person-name { color: var(--green); font-size: 15px; font-weight: 600; }
  .person-title { font-size: 13px; }
  .person-rule {
    position: absolute; left: 30px; top: 114px;
    width: 465px; height: 1px; background: var(--rule);
  }
  .back-brand {
    position: absolute; right: 30px; top: 62px;
    font-size: 30px; color: var(--green); font-weight: 400;
  }
  .contact {
    position: absolute; right: 30px; top: 150px;
    list-style: none; text-align: right;
    font-size: 13.5px; line-height: 21px;
  }
  .contact li { display: flex; justify-content: flex-end; align-items: center; gap: 8px; }
  .contact svg { width: 13px; height: 13px; flex: none; }
  .contact-rule {
    position: absolute; right: 30px; top: 138px;
    width: 220px; height: 1px; background: var(--rule);
  }
</style>
</head>
<body>
  <section class="card card-front">
    <div class="front-brand">Bramwell Pantry</div>
    <div class="front-tagline">Where good health meets real life</div>
  </section>

  <section class="card card-back">
    <svg class="back-wave" viewBox="0 0 525 300" aria-hidden="true">
      <path d="M0 120 C 90 110, 180 200, 300 240 C 380 265, 450 262, 525 258 L525 300 L0 300 Z" fill="var(--green)"/>
      <path d="M0 112 C 95 100, 185 190, 305 230 C 385 255, 455 254, 525 250 L525 258 C 450 262, 380 265, 300 240 C 180 200, 90 110, 0 120 Z" fill="var(--ink)"/>
      <path d="M0 126 C 90 118, 178 205, 298 246 C 378 272, 450 270, 525 266 L525 272 C 450 276, 376 278, 296 252 C 176 212, 88 126, 0 134 Z" fill="var(--paper)"/>
    </svg>

    <div class="person">
      <div class="person-name">Harriet Dunmore</div>
      <div class="person-title">Health Coach</div>
    </div>
    <div class="person-rule"></div>

    <div class="back-brand">Bramwell Pantry</div>

    <div class="contact-rule"></div>
    <ul class="contact">
      <li>(555) 218-4476
        <svg viewBox="0 0 16 16"><circle cx="8" cy="8" r="8" fill="var(--green)"/><path d="M5 4.5h2l.7 2-1.2.8a5 5 0 0 0 2.2 2.2l.8-1.2 2 .7v2c0 .5-.4.8-.9.8A7 7 0 0 1 4.2 5.4c0-.5.3-.9.8-.9z" fill="#fff"/></svg>
      </li>
      <li>harriet@bramwellpantry-example.com
        <svg viewBox="0 0 16 16"><circle cx="8" cy="8" r="8" fill="var(--green)"/><rect x="4" y="5" width="8" height="6" fill="#fff"/><path d="M4 5l4 3.5L12 5" stroke="var(--green)" fill="none"/></svg>
      </li>
      <li>www.bramwellpantry-example.com
        <svg viewBox="0 0 16 16"><circle cx="8" cy="8" r="8" fill="var(--green)"/><circle cx="8" cy="8" r="4.5" fill="none" stroke="#fff"/><path d="M3.5 8h9M8 3.5c-2 2.5-2 6.5 0 9M8 3.5c2 2.5 2 6.5 0 9" stroke="#fff" fill="none" stroke-width=".8"/></svg>
      </li>
    </ul>
  </section>
</body>
</html>
```